I need a simple infographic that describes the 4 basic elements of how to effectively create change.

The overall title (Gentle Pressure Relentlessly Applied) should be at the top of the infographic. Subtitle is: "Leading Change".
There are four steps:
1. Alignment- Agreement on Approach
2. Transparency- Metrics for Assurance
3. Skills- Training and Coaching
4. Integrity- Culture of Accountability

Target Market(s)

Business Leaders in a training workshop

Font styles to use
Serif

Requirements
Must have
• Here are the 4 elements of the Infographic: Please show them in order.
• 1. Agreement on Approach. (Alignment)
• 2. Metrics for Assurance (Transparency)
• 3. Training and Coaching (Skills)
• 4. Culture of Accountability (Integrity)
Nice to have
• Cool Graphics that depict the 4 steps.
Should not have
• Pictures.

```html
<!DOCTYPE html>
<html lang="en">
<head>
<meta charset="utf-8">
<title>Gentle Pressure Relentlessly Applied — Leading Change</title>
<link href="https://fonts.googleapis.com/css2?family=Montserrat:wght@300;400;700;800&display=swap" rel="stylesheet">
<style>
  :root {
    --canvas: #ecebe8;
    --ink: #0b0b0b;
    --white: #ffffff;
    --paper-top: #dfe2e6;
    --paper-bottom: #f7f7f8;
    --align-a: #ff4f63;
    --align-b: #ffc94a;
    --trans-a: #d060a8;
    --trans-b: #ff3a4d;
    --skills-a: #1f3f9e;
    --skills-b: #9866b4;
    --integ-a: #0fb39a;
    --integ-b: #1a5fc8;
  }
  * { margin: 0; padding: 0; box-sizing: border-box; }
  html, body { width: 1200px; height: 1200px; overflow: hidden; background: var(--canvas); }
  .poster {
    position: absolute; left: 171px; top: 10px; width: 858px; height: 1180px;
    background: linear-gradient(180deg, var(--paper-top) 0%, #eceef1 60%, var(--paper-bottom) 100%);
    font-family: 'Montserrat', sans-serif; overflow: hidden;
  }
  .poster-header {
    position: absolute; left: 0; top: 0; width: 100%; height: 152px; background: var(--ink);
    display: flex; align-items: center; justify-content: center; gap: 14px;
  }
  .brand-mark { width: 58px; height: 58px; border-radius: 50%; border: 3px solid var(--white); }
  .brand-name { color: var(--white); font-size: 36px; font-weight: 400; letter-spacing: -0.5px; }
  .backdrop { position: absolute; left: 0; top: 152px; }
  .headline {
    position: absolute; top: 186px; left: 0; width: 100%; text-align: center;
    font-weight: 800; font-size: 50px; line-height: 48px; letter-spacing: 1px; color: var(--ink);
  }
  .headline-rule { position: absolute; top: 298px; left: 289px; width: 280px; height: 1.5px; background: var(--ink); }
  .subtitle {
    position: absolute; top: 310px; left: 0; width: 100%; text-align: center;
    font-size: 25px; font-weight: 400; letter-spacing: 1.5px; color: var(--ink);
  }
  .steps { position: absolute; left: 0; top: 0; }
  .step-title { font-weight: 800; font-size: 30px; fill: var(--white); letter-spacing: 1px; }
  .step-sub { font-weight: 300; font-size: 19.5px; fill: var(--white); letter-spacing: 0.5px; }
</style>
</head>
<body>
<div class="poster">
  <svg class="backdrop" width="858" height="1028" viewBox="0 0 858 1028" aria-hidden="true">
    <path d="M0 420 C 140 240, 200 100, 170 0 L 250 0 C 250 120, 160 300, 0 520 Z" fill="#ffffff" opacity="0.45"/>
    <path d="M858 360 C 700 520, 520 600, 380 640 L 858 560 Z" fill="#ffffff" opacity="0.35"/>
    <path d="M0 910 C 300 880, 600 880, 858 920 L 858 1028 L 0 1028 Z" fill="#ffffff" opacity="0.9"/>
  </svg>

  <header class="poster-header">
    <span class="brand-mark"></span>
    <span class="brand-name">THE HARLOW GROUP</span>
  </header>

  <h1 class="headline">GENTLE PRESSURE<br>RELENTLESSLY APPLIED</h1>
  <div class="headline-rule"></div>
  <p class="subtitle">LEADING CHANGE</p>

  <svg class="steps" width="858" height="1180" viewBox="0 0 858 1180">
    <defs>
      <linearGradient id="grad-align" x1="0" x2="1"><stop offset="0" stop-color="var(--align-a)"/><stop offset="1" stop-color="var(--align-b)"/></linearGradient>
      <linearGradient id="grad-trans" x1="0" x2="1"><stop offset="0" stop-color="var(--trans-a)"/><stop offset="1" stop-color="var(--trans-b)"/></linearGradient>
      <linearGradient id="grad-skills" x1="0" x2="1"><stop offset="0" stop-color="var(--skills-a)"/><stop offset="1" stop-color="var(--skills-b)"/></linearGradient>
      <linearGradient id="grad-integ" x1="0" x2="1"><stop offset="0" stop-color="var(--integ-a)"/><stop offset="1" stop-color="var(--integ-b)"/></linearGradient>
    </defs>

    <g class="step step-alignment">
      <polygon points="229,433 733,433 780,509 733,585 229,585 274,509" fill="url(#grad-align)"/>
      <text class="step-title" x="305" y="505">ALIGNMENT</text>
      <text class="step-sub" x="305" y="528">AGREEMENT ON APPROACH</text>
      <circle cx="692" cy="504" r="36" fill="none" stroke="var(--white)" stroke-width="3"/>
      <circle cx="692" cy="504" r="31" fill="var(--white)" opacity="0.25"/>
      <g fill="var(--white)">
        <rect x="673" y="490" width="38" height="5"/><rect x="673" y="499" width="38" height="5"/>
        <rect x="673" y="508" width="38" height="5"/><rect x="673" y="517" width="38" height="5"/>
      </g>
    </g>

    <g class="step step-transparency">
      <polygon points="116,585 625,585 578,661 625,738 116,738 71,661" fill="url(#grad-trans)"/>
      <text class="step-title" x="244" y="658">TRANSPARENCY</text>
      <text class="step-sub" x="244" y="683">METRICS FOR ASSURANCE</text>
      <circle cx="154" cy="660" r="36" fill="none" stroke="var(--white)" stroke-width="3"/>
      <g fill="none" stroke="var(--white)" stroke-width="3">
        <circle cx="158" cy="656" r="12"/><path d="M142 660 a14 14 0 0 0 22 12"/>
      </g>
    </g>

    <g class="step step-skills">
      <polygon points="226,738 733,738 782,816 733,893 226,893 271,816" fill="url(#grad-skills)"/>
      <text class="step-title" x="301" y="808">SKILLS</text>
      <text class="step-sub" x="301" y="835">TRAINING AND COACHING</text>
      <circle cx="684" cy="817" r="36" fill="none" stroke="var(--white)" stroke-width="3"/>
      <circle cx="684" cy="817" r="30" fill="var(--white)" role="img" aria-label="Icon of a coach beside a puzzle board"/>
    </g>

    <g class="step step-integrity">
      <polygon points="104,893 618,893 571,972 618,1048 104,1048 59,972" fill="url(#grad-integ)"/>
      <text class="step-title" x="215" y="970">INTEGRITY</text>
      <text class="step-sub" x="215" y="997">CULTURE OF ACCOUNTABILITY</text>
      <circle cx="145" cy="972" r="36" fill="none" stroke="var(--white)" stroke-width="3"/>
      <circle cx="145" cy="972" r="30" fill="var(--white)" opacity="0.35" role="img" aria-label="Icon of a handshake"/>
    </g>
  </svg>
</div>
</body>
</html>
```